Design für satanierte Visitenkarten (transparent)
Zielgruppe
Wir sind ein Online Bildportal, bei dem man wie z. B. Pixanda, Lumoraframes und Brightcrate Bilder hochladen und verkaufen kann.
Unterschied zu den o. g. Portalen ist, dass wir uns auf den Exklusivmarkt fokusieren und der Künstler mind. 50% des Umsatzes erhält. Wichtig ist uns, dass sowohl der Kunde als auch der Fotograf/Grafiker Gewinner bei dem Handel sind (Win-Win-Situation)
Unsere Zeilgruppen:
Anbieter: Fotografen, Hobbyfotografen und Grafiker
Kunden: Marketingfirmen jeglicher Art
Aufgabenstellung
Wir benötigen ein Visitenkarten-Design, welches auf satinierte PVC-Visitenkarten (transparent) mit abgerundeten Ecken aufgedruckt wird. In der Design-Datei müssen sämtliche Variablen wie Name, Tel. etc. durch kurzes anklicken und reinschreiben austauschbar sein.
Unser Logo muss miteingebunden werden und sollte schön groß zu erkennen sein. Sollten dennoch Ideen aufkommen, bei denen dies etwas anders aussieht, lassen wir uns gerne überraschen.
Da das Ganze auf transparente Visitenkarten kommt, möchten wir, dass der Hintergrund beim Logo frei bleibt. Ein farbiger Hintergrund bei den Infos ist ok. Ein Hintergrund mit dem Farbcode #ededed wäre sehr passend, da sich auf der Webseite ebenfalls ein Balken mit abgerundeten Ecken befindet, welcher diesen Farbcode enthält.
Folgende Infos sollten enthalten sein:
- Name
- Position (Geschäftsführer etc.)
- Adresse
- Tel.
- Fax.
- Email
- Webadresse
Die Visitenkarten werden folgende Maße aufweisen:
Entwurfformat: 9 x 6 cm
Entformat: 8,5 x 5,5 cm
Folgende Punkte müssen laut Pruckerei beachtet werden:
Dateiformat: Das beste Druckergebnis erhalten Sie mit Vorlagen im Vektorformat (.ai und .eps ). Bitte senden Sie uns die Datei mit offenen Ebenen, die Texte in Pfade gewandelt oder gerastert (ansonsten ggf. den Font separat. Dies gilt auch für PDFs, da der Druck mit Illustrator vorbereitet wird!). Die Erstellung einer Stanzform oder eines Prägeklischees ist nur mit Vektordaten möglich.
Farbraum: Senden Sie uns die Daten unbedingt in CMYK (Coated FOGRA27). Die Umwandlung von RGB- in CMYK-Daten kann zu Farbabweichungen führen, daher nehmen Sie die Umwandlung bitte ggf. vor der Einsendung Ihrer Datei selbst vor. Wenn Ihr Design weiße Elemente enthalten soll, können Sie diese in 100% Cyan anlegen. Bitte fügen Sie dann eine Notiz wie "Cyan = Weiß" bei.
Beschnittzugabe: Zur Gestaltung von..

```html
<!DOCTYPE html>
<html lang="de">
<head>
<meta charset="utf-8">
<title>fotarion – Visitenkarte</title>
<link rel="stylesheet" href="https://fonts.googleapis.com/css2?family=Crimson+Pro:wght@400;600;700&display=swap">
<style>
  :root {
    --stage: #8c8c8c;
    --card: #c8c8c8;
    --card-light: #d2d2d2;
    --ink: #231f1c;
    --plum: #a3436a;
    --name-blue: #3a5f91;
    --serif: "Crimson Pro", Georgia, serif;
  }
  html, body {
    margin: 0;
    width: 1200px;
    height: 1200px;
    overflow: hidden;
    background: var(--stage);
  }
  .business-card {
    position: absolute;
    left: 100px;
    top: 276px;
    width: 1000px;
    height: 648px;
    border-radius: 36px;
    overflow: hidden;
    background: linear-gradient(120deg, var(--card) 0%, var(--card-light) 45%, var(--card) 100%);
    font-family: var(--serif);
    color: var(--ink);
  }
  .brand-name {
    position: absolute;
    left: 195px;
    top: 110px;
    margin: 0;
    font-size: 170px;
    font-weight: 600;
    line-height: 1;
    color: var(--ink);
    letter-spacing: -2px;
  }
  .divider {
    position: absolute;
    top: 328px;
    height: 18px;
  }
  .divider--dark { left: 0; width: 562px; background: var(--ink); }
  .divider--plum { left: 580px; width: 418px; background: var(--plum); }

  .person {
    position: absolute;
    left: 48px;
    top: 370px;
  }
  .person__first {
    display: block;
    font-size: 50px;
    line-height: 54px;
    color: var(--name-blue);
  }
  .person__last {
    display: block;
    font-size: 50px;
    line-height: 54px;
    font-weight: 700;
    color: var(--name-blue);
    letter-spacing: 0.5px;
  }
  .person__role {
    display: block;
    margin-top: 8px;
    font-size: 36px;
    line-height: 40px;
  }

  .contact {
    position: absolute;
    left: 596px;
    top: 364px;
    font-size: 35px;
    line-height: 38px;
  }
  .contact p { margin: 0; }
  .contact__group + .contact__group { margin-top: 6px; }
  .contact__web { font-weight: 700; }

  .shard-scatter {
    position: absolute;
    left: 130px;
    top: 548px;
    width: 455px;
    height: 100px;
  }
</style>
</head>
<body>
  <div class="business-card">
    <h1 class="brand-name">fotarion</h1>

    <div class="divider divider--dark"></div>
    <div class="divider divider--plum"></div>

    <div class="person">
      <span class="person__first">Lukas</span>
      <span class="person__last">BRANDNER</span>
      <span class="person__role">Geschäftsführer</span>
    </div>

    <div class="contact">
      <div class="contact__group">
        <p>Ahornwinkel 17</p>
        <p>81245 München</p>
      </div>
      <div class="contact__group">
        <p>Tel. +49 (0)89 47215038</p>
        <p>Fax +49 (0)89 47215099</p>
      </div>
      <div class="contact__group">
        <p>kontakt@fotarion.com</p>
        <p class="contact__web">www.fotarion.com</p>
      </div>
    </div>

    <svg class="shard-scatter" role="img" aria-label="Scattered colourful triangle shards decoration" viewBox="0 0 455 100" preserveAspectRatio="none">
      <defs>
        <linearGradient id="shard-tones" x1="0" y1="0" x2="1" y2="0">
          <stop offset="0" stop-color="#2a9fd8" stop-opacity="0.35"/>
          <stop offset="0.4" stop-color="#d6dc2a" stop-opacity="0.35"/>
          <stop offset="0.75" stop-color="#ee7a34" stop-opacity="0.35"/>
          <stop offset="1" stop-color="#e8303f" stop-opacity="0.35"/>
        </linearGradient>
      </defs>
      <rect width="455" height="100" fill="url(#shard-tones)"/>
    </svg>
  </div>
</body>
</html>
```